Business Card Design

We need a new buisness card designed for a new company in Darwin
We dig trenchs and lay pipes for the communication industry,Electrical industry, Teleco industry,
We also do some concrete works as well,
And small excavation work
Communication
Belvanti Contracting PTY LTD
Pit and Pipe installations
Trenching,Excavations, Concreting ,
civil works, unistrut soloutions ,over thirty years experiance
WHERE NOT FAZED WE WILL LAY ANYTHING
Contact Glen 0491536208 ps
(would like name to stand out somehow in another text or graphic sort of a way am also looking for some sort of slogan) will most likely be a red card with black writing

```html
<!DOCTYPE html>
<html lang="en">
<head>
<meta charset="utf-8">
<title>Belvanti Contracting PTY LTD – Business Card</title>
<link href="https://fonts.googleapis.com/css2?family=Open+Sans:ital,wght@1,700&display=swap" rel="stylesheet">
<style>
  :root {
    --red-deep: #5e0000;
    --red-mid: #b30000;
    --red-bright: #f01010;
    --ink: #000000;
    --paper: #ffffff;
  }
  html, body {
    margin: 0;
    padding: 0;
    overflow: hidden;
    background: #ffffff;
  }
  .card {
    position: relative;
    width: 1200px;
    height: 687px;
    overflow: hidden;
    font-family: "Open Sans", Arial, sans-serif;
    font-style: italic;
    font-weight: 700;
  }
  .card__backdrop {
    position: absolute;
    inset: 0;
    background:
      radial-gradient(ellipse 60% 55% at 70% 45%, rgba(255, 60, 60, 0.55), transparent 70%),
      radial-gradient(ellipse 50% 40% at 20% 85%, rgba(255, 40, 40, 0.35), transparent 70%),
      linear-gradient(120deg, var(--red-deep) 0%, var(--red-mid) 35%, var(--red-bright) 70%, var(--red-mid) 100%);
  }
  .brand-mark {
    position: absolute;
    left: 98px;
    top: 66px;
    width: 70px;
    height: 70px;
    border-radius: 50%;
    border: 4px solid var(--paper);
    box-sizing: border-box;
  }
  .company-name {
    position: absolute;
    left: 222px;
    top: 76px;
    margin: 0;
    font-size: 64px;
    line-height: 1;
    color: var(--paper);
    white-space: nowrap;
    letter-spacing: -0.5px;
  }
  .header-rule {
    position: absolute;
    left: 0;
    top: 172px;
    width: 1187px;
    height: 3px;
    background: var(--ink);
  }
  .services {
    position: absolute;
    left: 0;
    top: 264px;
    width: 1208px;
    margin: 0;
    padding: 0;
    list-style: none;
    text-align: center;
    color: var(--ink);
    font-size: 33px;
    line-height: 50px;
    letter-spacing: -0.4px;
  }
  .services__slogan {
    text-transform: uppercase;
    letter-spacing: -0.6px;
  }
  .contact {
    position: absolute;
    left: 455px;
    top: 570px;
    margin: 0;
    font-size: 51px;
    line-height: 1;
    color: var(--paper);
    white-space: nowrap;
    letter-spacing: -0.3px;
  }
</style>
</head>
<body>
  <div class="card">
    <div class="card__backdrop" role="img" aria-label="Red background with glitter sparkles and flowing wave lines"></div>

    <span class="brand-mark" aria-hidden="true"></span>
    <h1 class="company-name">Belvanti Contracting PTY LTD</h1>
    <div class="header-rule"></div>

    <ul class="services">
      <li>Pit and Pipe installation Specialist,</li>
      <li>Trenching,Excavations,</li>
      <li>And a little bit of concreting</li>
      <li class="services__slogan">Where not fazed we will lay anything</li>
    </ul>

    <p class="contact">Contact - Glen 0491536208</p>
  </div>
</body>
</html>
```